Etiketten für Hersteller und Vertreiber von Tierpflegeprodukten
Zielgruppe
hersteller und vertreiber von tierpflegeprodukten, Absatz hauptsächlich über das Internet (Online-Shop), Angebot reicht von hochwertigen Bio-Artikeln, über konventionelle Pflegeprodukte bis hin zu spezial Produkten wie für Hundesalons oder hypoallergene Pflegeprodukte
Ziel: weit gefächert, alle Tierbesitzer von Hunden/Katzen/Pferden und weiteren Kleintieren
kleine Gebinde von 100ml oder 200ml über 500ml bis zu 2l / Professionelle Produkte: 5l und 20l
Angedacht sind drei Sprachen: französisch vordergründig, zudem klein englisch und spanisch (Texte sind vorhanden)
Aufgabenstellung
gerade die Etiketten von den kleinen Gebinden (100ml) betragen nur 70x110 (in mm), der Hauptteil (Shampoo in 200ml) tragen eine Etikette der Größe 100x150, alles andere bekommt 120x150
auf dieser Fläche müß der Name 'VELUSIRANT' 'bio' deutlich zu sehen sein, Achtung, es sind Rundflaschen, desweiteren sollte eventuell der Wirkstoff (zB. Granatapfel) zu sehen sein (Abbildungen von jedem Wirkstoff/Pflanzenrohstoff sind exklusiv vorhanden)
Natürlich muss die Produktkategorie erscheinen (Shampoo / Spülung / Ohrenreiniger / Pfotencreme etc)
Auf der Rückseite kommt der Text zu dem Pflegeprodukt in den drei Sprachen (vorhanden) sowie weitere obligatorische Angaben und der BarCode
Im Onlineshop sind natürlich Abbildungen der Flaschen zu sehen: hier muss der Kunde es 'einladend / modern / bio / pflegend / exclusiv' finden
Als Datei füge ich 'Vorstellungen' über den Gebrauch der Marke ein / unsere 'Versuche' die nicht uns zufriedenstellten / ein Bild von der Rundflsche mit den entsprechenden 'Versuchen'
Der Name atelier sol montevu kann vernachlässigt werden, er ist nicht wichtig. Wichtig ist wirklich die Frontseite

```html
<!DOCTYPE html>
<html lang="fr">
<head>
<meta charset="utf-8">
<title>VELUSIRANT bio – Etiketten</title>
<link href="https://fonts.googleapis.com/css2?family=Open+Sans:wght@400;600&family=PT+Sans+Narrow:wght@400&family=Playfair+Display:ital@1&display=swap" rel="stylesheet">
<style>
  :root {
    --page: #ffffff;
    --label: #f3f3f3;
    --ink: #2b2b2b;
    --brand: #333333;
    --band-line: #ece4b0;
    --cat-band: #a3bba3;
    --cat-bio: #94c1a7;
    --cat-moon: #e9e6b8;
    --cat-rule: #8fb5a0;
    --dog-band: #a8c1c9;
    --dog-bio: #9fc4cd;
    --dog-moon: #dfe8e3;
    --dog-rule: #93b7c2;
    --horse-band: #df7c6f;
    --horse-bio: #e5695e;
    --horse-moon: #efc98c;
    --horse-rule: #e2675b;
  }
  * { box-sizing: border-box; margin: 0; padding: 0; }
  html, body { width: 1200px; height: 848px; overflow: hidden; background: var(--page); }
  body { font-family: "Open Sans", sans-serif; color: var(--ink); }

  .label-row {
    position: absolute; left: 90px; top: 140px;
    display: flex; gap: 60px;
  }
  .label {
    width: 300px; height: 570px;
    background: var(--label);
    display: flex; flex-direction: column; align-items: center;
    padding-top: 22px;
  }
  .brand {
    font-weight: 400; font-size: 25px; letter-spacing: 3px;
    color: var(--brand); line-height: 1.2;
  }
  .visual { position: relative; width: 290px; height: 226px; margin-top: 14px; }
  .bio {
    position: absolute; left: 50%; top: 0; transform: translateX(-50%);
    width: 80px; height: 80px; border-radius: 50%;
    display: flex; align-items: center; justify-content: center;
    font-family: "Playfair Display", serif; font-style: italic;
    font-size: 38px; color: #fff; z-index: 1;
  }
  .ingredient-art {
    position: absolute; left: 4px; right: 4px; top: 40px; bottom: 0;
    border-radius: 50%;
  }
  .product-name {
    margin-top: 8px; font-weight: 600; font-size: 24px; letter-spacing: 1px;
    padding: 0 8px 2px; border-bottom: 2px solid; line-height: 1.2;
  }
  .active { font-size: 19px; margin-top: 3px; line-height: 1.2; }
  .category {
    font-family: "PT Sans Narrow", sans-serif; font-size: 13.5px;
    margin-top: 8px; letter-spacing: .2px;
  }

  .band {
    margin-top: 8px; width: 100%; height: 178px;
    display: grid; grid-template-columns: 1fr 112px 1fr; align-items: center;
    font-family: "PT Sans Narrow", sans-serif; text-align: center; padding: 0 4px;
  }
  .band-col { display: flex; flex-direction: column; gap: 4px; }
  .band-col p { font-size: 16px; line-height: 1.1; padding-bottom: 4px; }
  .band-col p + p { border-top: 1.5px solid var(--band-line); padding-top: 6px; }
  .band-col .small { font-size: 11px; }
  .animal { width: 108px; height: 108px; border-radius: 50%; justify-self: center; }

  .cat .bio { background: var(--cat-bio); }
  .cat .product-name { border-color: var(--cat-rule); }
  .cat .band { background: var(--cat-band); }
  .cat .animal { background: radial-gradient(circle at 62% 55%, var(--cat-moon) 60%, #b9b88f 100%); }
  .cat .ingredient-art { background: radial-gradient(ellipse at center, #ece6a4 0%, #c9d48a 35%, #7eaa58 58%, rgba(243,243,243,0) 70%); }

  .dog .bio { background: var(--dog-bio); }
  .dog .product-name { border-color: var(--dog-rule); }
  .dog .band { background: var(--dog-band); }
  .dog .animal { background: radial-gradient(circle at 62% 55%, var(--dog-moon) 60%, #b9c9c6 100%); }
  .dog .ingredient-art { background: radial-gradient(ellipse at center, #d2e2aa 0%, #9cc171 35%, #5f9747 58%, rgba(243,243,243,0) 70%); }

  .horse .bio { background: var(--horse-bio); }
  .horse .product-name { border-color: var(--horse-rule); }
  .horse .band { background: var(--horse-band); }
  .horse .animal { background: radial-gradient(circle at 55% 55%, var(--horse-moon) 60%, #c99a62 100%); }
  .horse .ingredient-art { background: radial-gradient(ellipse at 60% 55%, #b08050 0%, #9cc065 35%, #627d3e 58%, rgba(243,243,243,0) 70%); }
</style>
</head>
<body>
<main class="label-row">

  <section class="label cat">
    <div class="brand">VELUSIRANT</div>
    <div class="visual">
      <div class="bio">bio</div>
      <div class="ingredient-art" role="img" aria-label="Blühender Hennastrauch mit gelben Blüten und grünen Blättern"></div>
    </div>
    <h2 class="product-name">LUMINEUX</h2>
    <div class="active">Hennè neutre</div>
    <div class="category">SHAMPOOING SPECIAUX POUR CHAT</div>
    <div class="band">
      <div class="band-col">
        <p>for<br>shiny coat</p>
        <p>Neutral<br>Henna</p>
        <p class="small">Special Care<br>Shampoo for cats</p>
      </div>
      <div class="animal" role="img" aria-label="Silhouette einer sitzenden Katze vor einem hellen Mond"></div>
      <div class="band-col">
        <p>für<br>mehr Glanz</p>
        <p>Neutrales<br>Henna</p>
        <p class="small">Pflege-Shampoo<br>für Katzen</p>
      </div>
    </div>
  </section>

  <section class="label dog">
    <div class="brand">VELUSIRANT</div>
    <div class="visual">
      <div class="bio">bio</div>
      <div class="ingredient-art" role="img" aria-label="Brennnesselzweig mit gezackten Blättern und Blütenrispen"></div>
    </div>
    <h2 class="product-name">AMPLITUDE</h2>
    <div class="active">Grand Ortie</div>
    <div class="category">SHAMPOOING SPECIAUX POUR CHIENS</div>
    <div class="band">
      <div class="band-col">
        <p>for more<br>volume</p>
        <p>Stinging<br>nettle</p>
        <p class="small">Special Care<br>Shampoo for dogs</p>
      </div>
      <div class="animal" role="img" aria-label="Silhouette eines sitzenden Hundes vor einem hellen Mond"></div>
      <div class="band-col">
        <p>für mehr<br>Haarvolumen</p>
        <p>Brennnessel</p>
        <p class="small">Pflege-Shampoo<br>für Hunde</p>
      </div>
    </div>
  </section>

  <section class="label horse">
    <div class="brand">VELUSIRANT</div>
    <div class="visual">
      <div class="bio">bio</div>
      <div class="ingredient-art" role="img" aria-label="Walnüsse mit grüner Schale, Teeblätter und getrockneter schwarzer Tee"></div>
    </div>
    <h2 class="product-name">ROBE ÉBÈNE</h2>
    <div class="active">Noir et Thé noir</div>
    <div class="category">SHAMPOOING SPECIAUX POUR CHEVAL</div>
    <div class="band">
      <div class="band-col">
        <p>for<br>dark coat</p>
        <p>Walnut &amp;<br>black tea</p>
        <p class="small">Special Care<br>Shampoo for horses</p>
      </div>
      <div class="animal" role="img" aria-label="Silhouette eines galoppierenden Pferdes vor einer goldenen Sonne"></div>
      <div class="band-col">
        <p>für<br>dunkles Fell</p>
        <p>Walnuss &amp;<br>schwarzer Tee</p>
        <p class="small">Pflege-Shampoo<br>für Pferde</p>
      </div>
    </div>
  </section>

</main>
</body>
</html>
```